Pebble Brook Cafe Take Out Menu

We serve coffee and tea made from our very own reverse osmosis water. Serve sandwiches, soups, pastry and more. Christian company! Want a to go menu so it needs to be condensed from one I sent you.

Target Market(s)

Portales and Roosevelt County NM

Industry/Entity Type

Coffee Shop

```html
<!DOCTYPE html>
<html lang="en">
<head>
<meta charset="utf-8">
<title>Take Out Menu</title>
<link rel="stylesheet" href="https://fonts.googleapis.com/css2?family=Kalam:wght@700&family=Oswald:wght@300;400&family=Lobster+Two:ital,wght@1,700&display=swap">
<style>
:root{
  --ink:#2a2a2a;
  --red:#d8402a;
  --blue:#1f3f8f;
  --green:#3fa33a;
  --dot-blue:#2c53b8;
  --paper:#ffffff;
  --tint:#e9f0fb;
}
*{margin:0;padding:0;box-sizing:border-box}
html,body{width:778px;height:1200px;overflow:hidden;background:var(--paper)}
.menu{position:relative;width:778px;height:1200px;font-family:"Oswald",sans-serif;font-weight:300;color:var(--ink);background:
  repeating-linear-gradient(135deg,var(--tint) 0 6px,transparent 6px 14px) right top/120px 1200px no-repeat,var(--paper)}
.abs{position:absolute}
.photo{position:absolute;border-radius:40%;background:radial-gradient(circle at 45% 45%,#8cc850,#4f8e2b 60%,#e8efe0 100%)}
.banner-title{position:absolute;font-family:"Lobster Two",cursive;font-style:italic;font-weight:700;color:var(--blue);letter-spacing:4px;text-transform:uppercase}
.salads-box{left:14px;top:52px;width:752px;height:478px;border:5px dotted var(--green);border-radius:10px}
.item h3{font-family:"Kalam",cursive;font-weight:700;color:var(--red);font-size:29px;line-height:1.1;text-align:center}
.item p{font-size:19px;line-height:1.2;text-align:center}
.sides .item h3{text-align:left;display:inline;font-size:27px}
.sides .item{margin-bottom:10px;font-size:19px;line-height:1.2}
.wraps-box{left:508px;top:660px;width:258px;height:392px;border:5px dotted var(--dot-blue);border-radius:6px}
.wraps p{font-size:19px;line-height:1.2;text-align:center;margin-bottom:8px}
.wraps b{font-family:"Kalam",cursive;color:var(--red);font-size:24px}
.extras-tab{left:10px;top:1062px;width:40px;height:118px;background:var(--red);color:#fff;font-family:"Oswald",sans-serif;font-weight:400;font-size:22px;letter-spacing:3px;display:flex;align-items:center;justify-content:center}
.extras-tab span{transform:rotate(-90deg)}
.extras{left:60px;top:1064px;width:700px;display:flex;justify-content:space-between;font-size:20px;line-height:1.25}
.rule{position:absolute;height:0;border-top:4px dotted var(--green)}
</style>
</head>
<body>
<main class="menu">
  <div class="photo" style="left:-20px;top:-20px;width:170px;height:125px" role="img" aria-label="Photo of a fresh green salad"></div>
  <div class="photo" style="left:650px;top:-20px;width:150px;height:125px" role="img" aria-label="Photo of a salad bowl"></div>

  <section class="abs salads-box"></section>
  <svg class="abs" style="left:220px;top:40px" width="340" height="80" viewBox="0 0 340 80">
    <path d="M10 45 Q170 5 330 45" fill="none" stroke="var(--blue)" stroke-width="3"/>
    <path d="M10 70 Q170 40 330 70" fill="none" stroke="var(--blue)" stroke-width="3"/>
  </svg>
  <h1 class="banner-title" style="left:0;width:778px;top:48px;text-align:center;font-size:46px">Salads</h1>

  <div class="abs item" style="left:30px;top:130px;width:350px">
    <h3>Chef Salad</h3>
    <p>A generous bed of mixed green lettuce with ham, grilled chicken, bacon, shredded cheese, boiled egg, tomatoes, onion, cucumber, croûtons and your choice of dressing. $7.00</p>
  </div>
  <div class="abs item" style="left:30px;top:300px;width:350px">
    <h3>Grilled Chicken Salad</h3>
    <p>A generous bed of mixed green lettuce, grilled chicken, shredded cheese, tomatoes, onion, cucumbers, croûtons and your choice of dressing. $6.75</p>
  </div>
  <div class="abs item" style="left:400px;top:130px;width:345px">
    <h3>Pecan Chicken Salad</h3>
    <p>A generous portion of fresh green lettuce mix with a large scoop of our fresh homemade pecan chicken salad topped with tomatoes. $6.50</p>
  </div>
  <div class="abs item" style="left:400px;top:280px;width:345px">
    <h3>Tuna Salad</h3>
    <p>A generous portion of fresh green lettuce mix with a large scoop of our fresh homemade tuna salad topped with tomatoes. $6.50</p>
  </div>
  <div class="abs item" style="left:30px;top:448px;width:720px">
    <h3>Side Salad</h3>
    <p>A small lettuce and tomato side salad served with your choice of dressing. $3.00</p>
  </div>

  <h2 class="banner-title" style="left:30px;top:546px;font-size:36px;letter-spacing:3px">Soups</h2>
  <div class="rule" style="left:30px;top:598px;width:140px"></div>
  <p class="abs" style="left:190px;top:545px;width:560px;text-align:center;font-size:20px;line-height:1.25">Ask server for daily soup options<br>Available In 3 Sizes SM. $2.49 LG. $3.99 FAMILY $12.99</p>
  <div class="rule" style="left:190px;top:612px;width:575px"></div>

  <h2 class="banner-title" style="left:40px;top:630px;font-size:36px;letter-spacing:3px">Sides</h2>
  <div class="abs sides" style="left:30px;top:690px;width:460px">
    <div class="item"><h3>Guacamole &amp; Chips</h3><br>Made fresh daily and served with tortilla chips. Small $3.50 Large $4.95</div>
    <div class="item" style="padding-left:40px"><h3>Pasta Salad</h3> Small $1.25<br>Medium....$1.75 Large$2.25</div>
    <div class="item" style="padding-left:40px"><h3>Coleslaw</h3> Small $1.25<br>Medium $1.75 Large $2.25</div>
    <div class="item" style="padding-left:40px"><h3>Potato Salad</h3> Small $1.25<br>Medium....$1.75 Large $2.25</div>
    <div class="item"><h3>Fresh Fruit Cup</h3> Fresh fruit as available and in season! $2.50</div>
  </div>

  <section class="abs wraps-box"></section>
  <div class="photo" style="left:660px;top:625px;width:110px;height:65px" role="img" aria-label="Photo of a sliced wrap"></div>
  <div class="abs wraps" style="left:520px;top:668px;width:234px">
    <h2 class="banner-title" style="position:static;font-size:34px;letter-spacing:3px;text-align:center">Wraps</h2>
    <p style="color:var(--red);font-weight:400">~ $6.50 ~</p>
    <p>Choose From The Following</p>
    <p><b>Tortilla</b> Tomato Basil, Jalapeño Cheddar, Garlic Herb, Spinach</p>
    <p><b>Meat</b> Turkey, ham or roast beef Cheese: cheddar, pepper jack, Swiss or American</p>
    <p><b>Sauce</b> Mayo, Ranch, Honey Mustard, Mustard</p>
    <p><b>Veggies</b> lettuce, tomato, onion, cucumber, ranch dressing Served with chips.</p>
  </div>

  <div class="abs extras-tab"><span>EXTRAS</span></div>
  <div class="abs extras">
    <div>Gluten free bread 2.00<br>Cheese .50<br>Meat 1.50</div>
    <div>Green chili .50<br>Boiled egg 1.00<br>Extra dressing .75</div>
    <div style="text-align:center">Guacamole<br>(mini on side or on<br>sandwich/salad) 1.00</div>
  </div>
</main>
</body>
</html>
```